Young, dynamic furniture company needs a new business card design

We require a new business card design for our modern furniture company which supplies furniture and appliances to the property and development market.
Oakline Furnishings has become one of the leading furniture & appliance suppliers to the property market withing London. With over 10 years experience, we have increased our business to supply not only private landlords and managing agents, but also property developers, housing associations and local councils.
We offer not only a complete range of furniture which includes beds, wardrobes, dining sets and sofas, but also a high quality, full delivery and assembly service to help you with all our furnishing needs.

Target Market(s)

Private landlords, estate agents, letting agents, property management companies

Industry/Entity Type

Business

Contact Information for Business Card

Name,
Title,
Address,
Mobile,
Telephone,
Fax, Website, email address

Font styles to use
Sans Serif

Colors
3176b5
0555a3
85abd2
cfdeed

Requirements
Must have
• All the above information for each of our staff, along with our logo

```html
<!DOCTYPE html>
<html lang="en">
<head>
<meta charset="utf-8">
<title>Oakline Furnishings – Business Card</title>
<link rel="stylesheet" href="https://fonts.googleapis.com/css2?family=Oswald:wght@500;600&family=Roboto:wght@300;400;500&display=swap">
<style>
  :root {
    --ink: #222428;
    --navy: #0555a3;
    --blue: #3176b5;
    --sky: #85abd2;
    --mist: #cfdeed;
    --grey-band: #eceef1;
    --paper: #ffffff;
    --stage: #e9e6e1;
    --muted: #5a5d63;
  }
  * { box-sizing: border-box; margin: 0; padding: 0; }
  html, body { width: 1200px; height: 900px; overflow: hidden; }
  body {
    background: var(--stage);
    font-family: "Roboto", Arial, sans-serif;
    color: var(--ink);
    position: relative;
  }
  .card {
    position: absolute;
    width: 540px;
    height: 310px;
    background: var(--paper);
    overflow: hidden;
    box-shadow: 0 6px 18px rgba(0,0,0,0.18);
  }
  .card--front { left: 70px; top: 110px; }
  .card--back  { left: 590px; top: 470px; }

  .backdrop-band {
    position: absolute;
    inset: 0;
    width: 100%;
    height: 100%;
  }

  /* brand lockup */
  .brand { position: absolute; display: flex; align-items: center; gap: 10px; }
  .brand__square { width: 22px; height: 22px; background: var(--navy); flex: none; }
  .brand__text { display: flex; flex-direction: column; }
  .brand__name {
    font-family: "Roboto", Arial, sans-serif;
    font-weight: 400;
    font-size: 17px;
    letter-spacing: 0.5px;
    color: var(--ink);
    text-transform: uppercase;
    line-height: 1.1;
  }
  .brand__tagline {
    font-size: 8.5px;
    letter-spacing: 0.8px;
    color: var(--muted);
    text-transform: uppercase;
    margin-top: 3px;
  }
  .card--front .brand { left: 40px; top: 96px; }
  .card--back .brand { left: 50%; top: 50%; transform: translate(-50%, -50%); }
  .card--back .brand__name { font-size: 22px; }
  .card--back .brand__square { width: 28px; height: 28px; }

  .divider-line {
    position: absolute;
    left: 40px; right: 40px; top: 56px;
    height: 1px;
    background: var(--ink);
  }
  .divider-line--bottom { top: auto; bottom: 40px; }

  .person { position: absolute; left: 40px; top: 170px; }
  .person__name {
    font-family: "Oswald", "Arial Narrow", sans-serif;
    font-weight: 600;
    font-size: 22px;
    letter-spacing: 0.5px;
    text-transform: uppercase;
    color: var(--ink);
    line-height: 1.1;
  }
  .person__title {
    font-family: "Oswald", "Arial Narrow", sans-serif;
    font-weight: 500;
    font-size: 13px;
    text-transform: uppercase;
    color: var(--navy);
    letter-spacing: 0.6px;
  }

  .contacts {
    position: absolute;
    left: 260px; top: 150px;
    padding-left: 14px;
    border-left: 1px solid var(--ink);
    list-style: none;
  }
  .contacts__item {
    display: flex; align-items: center; gap: 8px;
    font-size: 13px; line-height: 22px; color: var(--ink);
  }
  .contacts__icon {
    width: 13px; height: 13px; flex: none;
    background: var(--blue); border-radius: 2px;
    display: flex; align-items: center; justify-content: center;
  }
  .contacts__icon svg { width: 9px; height: 9px; }
</style>
</head>
<body>

<article class="card card--front">
  <svg class="backdrop-band" viewBox="0 0 540 310" aria-hidden="true">
    <polygon points="0,70 330,70 230,310 0,310" fill="var(--grey-band)"/>
    <polygon points="330,0 540,0 540,120 290,120" fill="var(--mist)" opacity="0.45"/>
  </svg>
  <div class="divider-line"></div>
  <div class="brand">
    <span class="brand__square"></span>
    <div class="brand__text">
      <span class="brand__name">Oakline Furnishings</span>
      <span class="brand__tagline">Trade Furniture Solutions</span>
    </div>
  </div>
  <div class="person">
    <p class="person__name">Daniel Hart</p>
    <p class="person__title">Manager</p>
  </div>
  <ul class="contacts">
    <li class="contacts__item">
      <span class="contacts__icon"><svg viewBox="0 0 10 10"><path d="M2 1h2l1 2-1 1a5 5 0 0 0 2 2l1-1 2 1v2c-4 0-7-3-7-7z" fill="#fff"/></svg></span>
      0774-5550-1842
    </li>
    <li class="contacts__item">
      <span class="contacts__icon"><svg viewBox="0 0 10 10"><rect x="3" y="1" width="4" height="8" rx="1" fill="none" stroke="#fff"/></svg></span>
      0712-5550-3961
    </li>
    <li class="contacts__item">
      <span class="contacts__icon"><svg viewBox="0 0 10 10"><rect x="1" y="2.5" width="8" height="5" fill="none" stroke="#fff"/><path d="M1 2.5l4 3 4-3" fill="none" stroke="#fff"/></svg></span>
      dhart@mailbox.com
    </li>
    <li class="contacts__item">
      <span class="contacts__icon"><svg viewBox="0 0 10 10"><circle cx="5" cy="5" r="3.6" fill="none" stroke="#fff"/><path d="M1.4 5h7.2M5 1.4v7.2" stroke="#fff" stroke-width="0.8"/></svg></span>
      oaklinefurnishings.co.uk
    </li>
  </ul>
  <div class="divider-line divider-line--bottom"></div>
</article>

<article class="card card--back">
  <svg class="backdrop-band" viewBox="0 0 540 310" aria-hidden="true">
    <polygon points="0,0 300,0 200,150 0,150" fill="var(--grey-band)"/>
    <polygon points="200,150 540,100 540,200 120,250" fill="var(--grey-band)" opacity="0.8"/>
    <polygon points="300,190 430,190 400,310 330,310" fill="var(--mist)" opacity="0.5"/>
  </svg>
  <div class="brand">
    <span class="brand__square"></span>
    <div class="brand__text">
      <span class="brand__name">Oakline Furnishings</span>
      <span class="brand__tagline">Trade Furniture Solutions</span>
    </div>
  </div>
</article>

</body>
</html>
```